Business Card Design needed for logo design project

We need a business card design for a construction parts business.

We would like our main company logo on the front of the card and have our other company website logo on the rear of the card.

Both logos will be attached.

Front of card
Logo is KTR
Can we also have the wording "Construction Equipment Parts Specialists"
Main details to include:

Address:
Telephone:
Mobile:
Email:
Website:

Rear of card.

Logo is gearvaultdepot.com.au (we would like this logo taking up the most of the rear)
Also we want under gearvaultdepot.com.au the following wording "Parts Sourced For You From Across The Globe"
Updates

Please see new update for our design

Target Market(s)

Construction Industry.
Earthmoving Equipment owners.

Industry/Entity Type

Construction

Font styles to use
Sans Serif

Requirements
Must have
• Easy to read.
Clean and smart.
Should not have
• Should not have any colours other than the colours of our logos.

```html
<!DOCTYPE html>
<html lang="en">
<head>
<meta charset="utf-8">
<title>KTR Business Card</title>
<link href="https://fonts.googleapis.com/css2?family=Barlow+Condensed:wght@500;600&family=Open+Sans:wght@400;700&family=Questrial&display=swap" rel="stylesheet">
<style>
  :root {
    --teal-dark: #144a5a;
    --sky-blue: #1ea2dc;
    --paper: #f7f7f5;
    --ink: #262626;
    --grey-text: #8c8c8c;
    --backdrop: #9a9a98;
  }
  * { margin: 0; padding: 0; box-sizing: border-box; }
  html, body { width: 1200px; height: 1000px; overflow: hidden; }
  body { background: var(--backdrop); position: relative; font-family: "Open Sans", sans-serif; }

  .card { position: absolute; left: 215px; width: 770px; height: 440px; overflow: hidden; }

  /* Rear */
  .card-rear { top: 40px; background: var(--teal-dark); }
  .rear-wordmark {
    position: absolute; left: 60px; top: 158px;
    font-family: "Barlow Condensed", sans-serif; font-weight: 600;
    font-size: 54px; letter-spacing: 1px; color: #ffffff; line-height: 1;
    white-space: nowrap;
  }
  .rear-tagline {
    position: absolute; left: 62px; top: 218px;
    font-family: "Barlow Condensed", sans-serif; font-weight: 500;
    font-size: 15px; letter-spacing: 3px; text-transform: uppercase;
    color: var(--sky-blue); white-space: nowrap;
  }
  .rear-mark {
    position: absolute; left: 625px; top: 160px;
    width: 76px; height: 76px; border-radius: 50%; background: var(--sky-blue);
  }

  /* Front */
  .card-front { top: 520px; background: var(--paper); }
  .front-block {
    position: absolute; left: 0; top: 70px; width: 80px; height: 160px;
    background: var(--teal-dark);
  }
  .front-logo { position: absolute; left: 115px; top: 105px; display: flex; align-items: center; gap: 14px; }
  .front-logo-name {
    font-family: "Open Sans", sans-serif; font-weight: 700;
    font-size: 80px; line-height: 1; color: var(--teal-dark); letter-spacing: 2px;
  }
  .front-logo-dot { width: 32px; height: 32px; border-radius: 50%; background: var(--sky-blue); }

  .contact-list { position: absolute; left: 395px; top: 110px; list-style: none; font-size: 18px; color: var(--ink); }
  .contact-list li { display: flex; line-height: 32px; white-space: nowrap; }
  .contact-label { width: 34px; text-align: center; }
  .contact-sep { width: 16px; }

  .side-bars { position: absolute; right: 0; top: 215px; display: flex; flex-direction: column; gap: 7px; }
  .side-bar { width: 72px; height: 26px; background: var(--teal-dark); }

  .front-tagline {
    position: absolute; left: 110px; bottom: 34px;
    font-family: "Questrial", sans-serif; font-size: 27px; color: var(--grey-text);
    white-space: nowrap;
  }
</style>
</head>
<body>
  <section class="card card-rear">
    <div class="rear-wordmark">GEARVAULTDEPOT.COM.AU</div>
    <div class="rear-tagline">Parts sourced for you from across the globe</div>
    <div class="rear-mark"></div>
  </section>

  <section class="card card-front">
    <div class="front-block"></div>
    <div class="front-logo">
      <span class="front-logo-name">KTR</span>
      <span class="front-logo-dot"></span>
    </div>
    <ul class="contact-list">
      <li><span class="contact-label">A</span><span class="contact-sep">:</span>your address here</li>
      <li><span class="contact-label">T</span><span class="contact-sep">:</span>+000 00 000</li>
      <li><span class="contact-label">M</span><span class="contact-sep">:</span>+0000 000 000</li>
      <li><span class="contact-label">E</span><span class="contact-sep">:</span>emailid@provider.com</li>
      <li><span class="contact-label">W</span><span class="contact-sep">:</span>www.domainname.com</li>
    </ul>
    <div class="side-bars">
      <div class="side-bar"></div>
      <div class="side-bar"></div>
      <div class="side-bar"></div>
      <div class="side-bar"></div>
      <div class="side-bar"></div>
    </div>
    <div class="front-tagline">Construction Equipment Parts Specialists</div>
  </section>
</body>
</html>
```